swimming pool Leak Detection Brochure

I would Like to create a pool leak detection brochure

Target Market(s)

High end Clients with inground swimming pools

Industry/Entity Type

Pool Service

Font styles to use
Other font styles liked:
• Im open to suggestions but using my website for ideas is suggested

Colors

Designer to choose colors to be used in the design.

Requirements
Must have
• Do you Have a Leak??
• Figuring out when your pool has a leak can be tough. Environmental factors do play a role in the water level, and just because your pool’s water is lower than normal does not mean it has a leak. Wind, humidity, and sun exposure all impact your rate of evaporation.
• Warning Signs of a Leak in Your Pool
• Your pool, fountain, or spa loses more than 1/4 an inch of water a day
• There are cracks in or around the pool decking
• You need to add water more than once a week
• Grass around the area is soggy
• Your pool deck is sinking or lifting
Nice to have
• PREPARING FOR A LEAK TEST
• To ensure you receive an accurate leak detection test, it is required that you have the pool vacuumed and cleaned beforehand. Dirt and debris in the pool can make it difficult to spot even large leaks. Likewise, the water should be as clear as possible. If your water is green it means mildew, algae, or fungi has infested it. Not only does this make it impossible to test for leaks, but it’s dangerous for our health. Finally our pool should be full to the normal level - we can’t find a leak that is not leaking! After your test, you will be confident knowing you have a pool/fountain/spa that is free of leaks or the Leak has been found and can be repaired Properly.

```html
<!DOCTYPE html>
<html lang="en">
<head>
<meta charset="utf-8">
<title>Pool Leak Detection Flyer</title>
<link rel="stylesheet" href="https://fonts.googleapis.com/css2?family=Crimson+Pro:wght@400;500&family=Permanent+Marker&family=Roboto+Condensed:wght@400;700&display=swap">
<style>
  :root {
    --navy: #0f2a6b;
    --orange: #d8502a;
    --teal: #1b8fae;
    --sky: #7fb3e6;
    --sea: #2f6fa0;
    --lawn: #4f8a3a;
    --paper: #f1f2f3;
    --ink: #2b2b2b;
    --stage: #2e2f31;
  }
  * { margin: 0; padding: 0; box-sizing: border-box; }
  html, body { width: 1200px; height: 1200px; overflow: hidden; background: var(--stage); }
  .flyer {
    position: absolute; left: 194px; top: 30px; width: 812px; height: 1140px;
    background: radial-gradient(ellipse at 40% 60%, #ffffff 0%, var(--paper) 55%, #dcdfe2 100%);
    overflow: hidden; font-family: "Crimson Pro", serif; color: var(--ink);
  }
  .hero { position: absolute; left: 0; top: 0; width: 812px; height: 560px; }
  .brand-badge {
    position: absolute; left: 24px; top: 355px; width: 242px; height: 242px; border-radius: 50%;
    background: #fff; border: 6px solid var(--teal); box-shadow: 0 0 0 4px var(--orange);
    display: flex; align-items: center; justify-content: center; text-align: center;
    font-family: "Crimson Pro", serif; font-weight: 500; font-size: 30px; line-height: 1.1; color: var(--navy);
  }
  .headline-lead { position: absolute; left: 258px; top: 540px; font-size: 44px; color: var(--navy); font-weight: 400; }
  .headline-leak {
    position: absolute; left: 196px; top: 580px; font-family: "Permanent Marker", cursive;
    font-size: 112px; line-height: 1.1; color: var(--orange); letter-spacing: 2px;
  }
  .intro { position: absolute; left: 42px; top: 718px; width: 482px; font-size: 12.6px; line-height: 16px; }
  .signs { position: absolute; top: 790px; list-style: none; font-size: 12.6px; line-height: 16px; }
  .signs li { position: relative; padding-left: 12px; margin-bottom: 8px; }
  .signs li::before { content: ""; position: absolute; left: 0; top: 6px; width: 4px; height: 4px; border-radius: 50%; background: var(--orange); }
  .signs-left { left: 42px; width: 236px; text-align: justify; }
  .signs-right { left: 302px; width: 230px; }
  .pipe-photo { position: absolute; left: 546px; top: 675px; width: 256px; height: 256px; border-radius: 50%; border: 6px solid var(--navy);
    background: radial-gradient(circle at 50% 60%, #9a9488 0%, #5e574e 55%, #3b352f 100%); }
  .prep-title { position: absolute; left: 47px; top: 928px; font-family: "Permanent Marker", cursive; font-size: 20px; color: var(--navy); letter-spacing: 1px; }
  .prep-body { position: absolute; left: 42px; top: 961px; width: 730px; font-size: 12.4px; line-height: 15.8px; }
  .footer { position: absolute; left: 0; top: 1050px; width: 812px; height: 90px; }
  .contacts { position: absolute; left: 48px; top: 1078px; display: flex; align-items: center; gap: 26px;
    font-family: "Roboto Condensed", sans-serif; color: #fff; }
  .contacts span { display: flex; align-items: center; gap: 7px; }
  .contacts svg { width: 17px; height: 17px; fill: none; stroke: #fff; stroke-width: 1.8; }
  .phone { font-weight: 700; font-size: 16px; }
  .email { font-size: 12px; }
  .web { font-size: 14.5px; }
  .license { font-size: 11.5px; }
</style>
</head>
<body>
<main class="flyer">
  <svg class="hero" viewBox="0 0 812 560" aria-hidden="false">
    <defs>
      <linearGradient id="heroTone" x1="0" y1="0" x2="0" y2="1">
        <stop offset="0" stop-color="var(--sky)"/>
        <stop offset="0.24" stop-color="#cfe0f0"/>
        <stop offset="0.26" stop-color="var(--sea)"/>
        <stop offset="0.36" stop-color="var(--lawn)"/>
        <stop offset="0.55" stop-color="#6a9e8c"/>
        <stop offset="1" stop-color="#c9b8a3"/>
      </linearGradient>
    </defs>
    <path role="img" aria-label="Photo of an infinity-edge pool beside a stone deck with lounge chairs, lawn and ocean view, with a leak detection kit bag on the deck"
          d="M0 0 H812 V500 C740 515 660 532 560 532 C470 532 400 492 267 456 L0 440 Z" fill="url(#heroTone)"/>
    <path d="M267 456 C400 492 470 532 560 532 C660 532 740 515 812 500" fill="none" stroke="var(--navy)" stroke-width="5"/>
    <path d="M267 462 C400 500 470 542 560 542 C660 542 740 525 812 510" fill="none" stroke="var(--orange)" stroke-width="6"/>
    <path d="M300 478 C420 512 480 552 565 552 C665 552 745 535 812 522" fill="none" stroke="var(--teal)" stroke-width="3" opacity="0.6"/>
  </svg>

  <div class="brand-badge">Harbor<br>Pool Service</div>

  <h1 class="headline-lead">Do you Have a</h1>
  <div class="headline-leak">LEAK??</div>

  <p class="intro">Figuring out when your pool has a leak can be tough. Environmental factors do play a role in the water level, and just because your pool’s water is lower than normal does not mean it has a leak. Wind, humidity, and sun exposure all impact your rate of evaporation.</p>

  <ul class="signs signs-left">
    <li>Warning Signs of a Leak in Your Pool</li>
    <li>Your pool, fountain, or spa loses more than 1/4 an inch of water a day</li>
    <li>There are cracks in or around the pool decking</li>
  </ul>
  <ul class="signs signs-right">
    <li>You need to add water more than once a week</li>
    <li>Grass around the area is soggy</li>
    <li>Your pool deck is sinking or lifting</li>
  </ul>

  <div class="pipe-photo" role="img" aria-label="Close-up photo of a leaking buried pipe in wet soil"></div>

  <h2 class="prep-title">PREPARING FOR A LEAK TEST</h2>
  <p class="prep-body">To ensure you receive an accurate leak detection test, it is required that you have the pool vacuumed and cleaned beforehand. Dirt and debris in the pool can make it difficult to spot even large leaks. Likewise, the water should be as clear as possible. If your water is green it means mildew, algae, or fungi has infested it. Not only does this make it impossible to test for leaks, but it’s dangerous for our health. Finally our pool should be full to the normal level - we can’t find a leak that is not leaking! After your test, you will be confident knowing you have a pool/fountain/spa that is free of leaks or the Leak has been found and can be repaired Properly.</p>

  <svg class="footer" viewBox="0 0 812 90">
    <path d="M0 30 Q0 12 30 10 Q406 -2 782 10 Q812 12 812 30 V90 H0 Z" fill="var(--orange)"/>
    <path d="M0 34 Q0 16 30 14 Q406 2 782 14 Q812 16 812 34 V90 H0 Z" fill="var(--teal)"/>
  </svg>
  <div class="contacts">
    <span class="phone"><svg viewBox="0 0 24 24"><path d="M5 3h4l2 5-2.5 1.5a11 11 0 0 0 6 6L16 13l5 2v4a2 2 0 0 1-2 2A17 17 0 0 1 3 5a2 2 0 0 1 2-2z"/></svg>401-555-0147</span>
    <span class="email"><svg viewBox="0 0 24 24"><rect x="3" y="5" width="18" height="14"/><path d="M3 5l9 8 9-8"/></svg>info@harborpoolri.com</span>
    <span class="web"><svg viewBox="0 0 24 24"><circle cx="12" cy="12" r="9"/><path d="M3 12h18M12 3c3 3 3 15 0 18M12 3c-3 3-3 15 0 18"/></svg>www.harborpoolri.com</span>
    <span class="license"><svg viewBox="0 0 24 24"><path d="M12 22s7-7 7-12a7 7 0 0 0-14 0c0 5 7 12 7 12z" fill="#fff"/><circle cx="12" cy="10" r="2.5" stroke="var(--teal)"/></svg>RI REG # 40517, CT License # SP1- PLM 0912734</span>
  </div>
</main>
</body>
</html>
```